Pell Consulting -New consulting business in architecture, urban planning, and real estate development

We need a stationery design, including logo, business cards, etc, work for a new consulting business that works in the world of architectural, urban planning and real estate development.

The name of the company is "Pell Consulting". Pell is my last name but it of course also has the meaning 'cool' and 'hip'.

Target Market(s)

The business will provide boutique consulting services to high end clients that may include property developers, cities, etc.

Industry/Entity Type

Consultant

Contact Information for Business Card

PELL Consulting
First Name Last Name
Title
Phone number
Address
Website
Optional: Twitter handle

Logo Text

PELL Consulting

Font styles to use
Sans Serif

Colors

Designer to choose colors to be used in the design.

Requirements
Must have
• Simple design
• Easy to read font
• Modern
• Elegance
• Nice font that can be used for future reports, letters, etc.
• Good colour scheme that allows for the elegance to come through
Should not have
• Complex design ideas
• Complex logos
• Not a corporate feel and look

```html
<!DOCTYPE html>
<html lang="en">
<head>
<meta charset="utf-8">
<title>Pell Consulting – Business Card</title>
<link rel="stylesheet" href="https://fonts.googleapis.com/css2?family=Montserrat:wght@600&family=Open+Sans:ital,wght@0,400;1,400&display=swap">
<style>
  :root {
    --backdrop: #151515;
    --card: #2b2a29;
    --card-edge: #353433;
    --ink-strong: #c9c9c9;
    --ink-soft: #8f8f8f;
    --ink-logo: #b5b5b5;
  }
  * { margin: 0; padding: 0; box-sizing: border-box; }
  html, body {
    width: 1200px;
    height: 900px;
    overflow: hidden;
    background: var(--backdrop);
  }
  .stage {
    position: relative;
    width: 1200px;
    height: 900px;
    display: flex;
    flex-direction: column;
    align-items: center;
    justify-content: center;
    gap: 40px;
  }
  .card {
    position: relative;
    width: 680px;
    height: 389px;
    background: var(--card);
    border: 1px solid var(--card-edge);
    border-radius: 22px;
  }
  .wordmark {
    position: absolute;
    display: flex;
    align-items: center;
    gap: 14px;
    white-space: nowrap;
    font-family: "Montserrat", sans-serif;
    font-weight: 600;
    color: var(--ink-logo);
    letter-spacing: 0.08em;
    text-transform: uppercase;
  }
  .wordmark-square {
    background: var(--ink-logo);
    flex: none;
  }
  .card--front .wordmark {
    left: 50%;
    top: 50%;
    transform: translate(-50%, -50%);
    font-size: 38px;
  }
  .card--front .wordmark-square { width: 32px; height: 32px; }
  .card--back .wordmark {
    right: 56px;
    top: 180px;
    font-size: 24px;
    gap: 12px;
  }
  .card--back .wordmark-square { width: 20px; height: 20px; }
  .contact {
    position: absolute;
    left: 50px;
    top: 56px;
    font-family: "Open Sans", sans-serif;
  }
  .contact-name {
    font-family: "Montserrat", sans-serif;
    font-weight: 600;
    font-size: 22px;
    color: var(--ink-strong);
    letter-spacing: 0.04em;
    text-transform: uppercase;
  }
  .contact-title {
    font-size: 15px;
    color: var(--ink-soft);
    font-style: italic;
    margin-bottom: 14px;
  }
  .contact-list { list-style: none; }
  .contact-item {
    display: flex;
    align-items: center;
    gap: 12px;
    font-size: 14px;
    color: var(--ink-soft);
    line-height: 28px;
  }
  .contact-icon { width: 13px; height: 13px; flex: none; }
  .address {
    position: absolute;
    right: 56px;
    bottom: 44px;
    font-family: "Open Sans", sans-serif;
    font-style: normal;
    font-size: 14px;
    line-height: 22px;
    color: var(--ink-soft);
    text-align: left;
  }
</style>
</head>
<body>
<main class="stage">
  <section class="card card--front" aria-label="Business card front">
    <div class="wordmark"><span class="wordmark-square"></span><span>Pell Consulting</span></div>
  </section>

  <section class="card card--back" aria-label="Business card back">
    <div class="contact">
      <h1 class="contact-name">Daniel Pell</h1>
      <p class="contact-title">Chief Executive Office</p>
      <ul class="contact-list">
        <li class="contact-item">
          <svg class="contact-icon" viewBox="0 0 16 16" aria-hidden="true"><path fill="#8f8f8f" d="M3.5 1h2.5l1.2 3.5-1.6 1.2a9 9 0 0 0 4.7 4.7l1.2-1.6L15 10v2.5A2.5 2.5 0 0 1 12.5 15 11.5 11.5 0 0 1 1 3.5 2.5 2.5 0 0 1 3.5 1z"/></svg>
          <span>555-014-2200</span>
        </li>
        <li class="contact-item">
          <svg class="contact-icon" viewBox="0 0 16 16" aria-hidden="true"><rect x="1" y="3" width="14" height="10" rx="1" fill="none" stroke="#8f8f8f" stroke-width="1.5"/><path d="M1.5 3.5 8 9l6.5-5.5" fill="none" stroke="#8f8f8f" stroke-width="1.5"/></svg>
          <span>contact@pellconsulting.com</span>
        </li>
        <li class="contact-item">
          <svg class="contact-icon" viewBox="0 0 16 16" aria-hidden="true"><circle cx="8" cy="8" r="6.5" fill="none" stroke="#8f8f8f" stroke-width="1.5"/><ellipse cx="8" cy="8" rx="2.8" ry="6.5" fill="none" stroke="#8f8f8f" stroke-width="1.2"/><path d="M1.5 8h13" stroke="#8f8f8f" stroke-width="1.2"/></svg>
          <span>www.pellconsulting.com</span>
        </li>
      </ul>
    </div>

    <div class="wordmark"><span class="wordmark-square"></span><span>Pell Consulting</span></div>

    <address class="address">No 12 Linden Street Ashby<br>Victoria 3360 Australia</address>
  </section>
</main>
</body>
</html>
```